Business card for Northland's Blue Wagon.

Good day i am looking for a business card design for my business.
The name of the business is Northland's Blue Wagon. It is a van rental business that provides a driver and helper to the customer. Customer have use to van for small moves, studio or 1 bedroom, Moving furniture like couch or kitchen cabinets.
We are available evenings, weekends and holidays.
the means to contact us is by phone at 628-947-2071; By emails at Oakridge@northlandsbluewagon.net; or by social media, Facelink and Snapgram.
You can see attached pictures of the van and or logo.

```html
<!DOCTYPE html>
<html lang="en">
<head>
<meta charset="utf-8">
<title>Northland's Blue Wagon – Business Card</title>
<link rel="stylesheet" href="https://fonts.googleapis.com/css2?family=Merriweather:wght@400;700;900&display=swap">
<style>
  :root {
    --backdrop: #6b6b6b;
    --card-white: #ffffff;
    --card-white-shade: #ececec;
    --leaf-blush: #f3ddd2;
    --card-black: #060606;
    --leaf-dark: #1d1413;
    --brand-red: #d0141c;
    --text-light: #f4f4f4;
  }
  * { box-sizing: border-box; margin: 0; padding: 0; }
  html, body { width: 1200px; height: 900px; overflow: hidden; }
  body {
    background: var(--backdrop);
    font-family: "Merriweather", Georgia, serif;
    position: relative;
  }
  .card {
    position: absolute;
    width: 620px;
    height: 354px;
    border-radius: 26px;
    overflow: hidden;
  }
  .card-front { left: 110px; top: 70px; background: var(--card-white); }
  .card-back { left: 470px; top: 476px; background: var(--card-black); color: var(--text-light); }
  .leaf-pattern { position: absolute; inset: 0; }
  .card-front .leaf-pattern {
    background: radial-gradient(circle at 50% 40%, var(--card-white) 0%, var(--card-white) 40%, var(--leaf-blush) 160%),
                linear-gradient(160deg, var(--card-white), var(--card-white-shade));
    opacity: .9;
  }
  .card-back .leaf-pattern {
    background: radial-gradient(circle at 50% 50%, var(--card-black) 30%, var(--leaf-dark) 120%);
  }
  .brand-mark {
    position: absolute; inset: 0;
    display: flex; align-items: center; justify-content: center; gap: 12px;
  }
  .brand-dot { width: 22px; height: 22px; border-radius: 50%; background: var(--brand-red); }
  .brand-name { color: var(--brand-red); font-weight: 700; font-size: 24px; letter-spacing: .5px; }
  .contact {
    position: absolute; inset: 0;
    display: flex; flex-direction: column; align-items: center; justify-content: center;
    text-align: center;
  }
  .tagline { font-weight: 700; font-size: 19px; letter-spacing: .4px; }
  .rule {
    width: 330px; height: 1px; margin: 12px 0;
    background: linear-gradient(90deg, transparent, var(--brand-red), transparent);
  }
  .contact-row { display: flex; align-items: center; gap: 12px; }
  .contact-row svg { flex: none; }
  .phone-number { font-size: 31px; font-weight: 700; letter-spacing: .5px; }
  .email { font-size: 17px; font-weight: 700; }
  .services { font-size: 15px; font-weight: 700; letter-spacing: .2px; }
  .social { display: flex; gap: 22px; margin-top: 14px; }
  .social-item { display: flex; align-items: center; gap: 7px; font-size: 12px; font-weight: 700; }
  .social-dot { width: 14px; height: 14px; border-radius: 50%; background: var(--brand-red); }
</style>
</head>
<body>
  <section class="card card-front">
    <div class="leaf-pattern" role="img" aria-label="Scattered pale blush maple leaf pattern"></div>
    <div class="brand-mark">
      <span class="brand-dot"></span>
      <span class="brand-name">Northland's Blue Wagon</span>
    </div>
  </section>

  <section class="card card-back">
    <div class="leaf-pattern" role="img" aria-label="Scattered dark brown maple leaf pattern"></div>
    <div class="contact">
      <p class="tagline">Your Friend With The Van</p>
      <div class="rule"></div>
      <div class="contact-row">
        <svg width="30" height="30" viewBox="0 0 24 24" aria-hidden="true">
          <path fill="var(--brand-red)" d="M6.6 10.8a15.1 15.1 0 0 0 6.6 6.6l2.2-2.2a1 1 0 0 1 1-.25 11.4 11.4 0 0 0 3.6.57 1 1 0 0 1 1 1V20a1 1 0 0 1-1 1A17 17 0 0 1 3 4a1 1 0 0 1 1-1h3.5a1 1 0 0 1 1 1c0 1.25.2 2.45.57 3.57a1 1 0 0 1-.25 1z"/>
          <path fill="none" stroke="var(--brand-red)" stroke-width="1.6" stroke-linecap="round" d="M14 3.5a7 7 0 0 1 6.5 6.5M14 7a3.5 3.5 0 0 1 3 3"/>
        </svg>
        <span class="phone-number">628-947-2071</span>
      </div>
      <div class="rule"></div>
      <div class="contact-row">
        <svg width="28" height="22" viewBox="0 0 28 22" aria-hidden="true">
          <rect x="1" y="3" width="26" height="18" rx="2" fill="var(--brand-red)"/>
          <path d="M2 5l12 9 12-9" fill="none" stroke="var(--card-black)" stroke-width="1.6"/>
        </svg>
        <span class="email">Oakridge@northlandsbluewagon.net</span>
      </div>
      <div class="rule"></div>
      <p class="services">Van Rental With Driver | Evening And Weekends</p>
      <div class="social">
        <span class="social-item"><span class="social-dot"></span>Facelink</span>
        <span class="social-item"><span class="social-dot"></span>Snapgram</span>
      </div>
    </div>
  </section>
</body>
</html>
```